Save the Date for 77th birthday fundraiser

We need a design for a Save the Date as we are preparing to celebrate our founder Dell Pembrook’s 77 birthday next year.
We would like a professional illustrated Save the Date with the theme “How it started, How it’s going”. Attached is a picture from the early 70’s and another one from yesterday. We want him to look his absolute best.
We need the date, location, and contact details to RSVP incorporated into the design:
April 9
Marlow Ainsley Hall, Austin Texas
team@guidewellpath.com
AND PLEASE REMEMBER THIS IS A SURPRISE!
We would also like to include elements that evoke what he does: Author (he’s published 2 books), Speaker (a microphone), Business Coach, and Entrepreneur.
Feelings we would like to evoke when people see the image: Would like people to think we are a professional company that is throwing a fun event for all the clients and friends Dell has made along his extraordinary 50-year career.
Thank you so much!

```html
<!DOCTYPE html>
<html lang="en">
<head>
<meta charset="utf-8">
<title>Dell Pembrook 77th Birthday – Save the Date</title>
<link href="https://fonts.googleapis.com/css2?family=Poppins:ital,wght@0,300;0,400;0,500;0,600;0,700;1,300;1,400;1,600;1,800&display=swap" rel="stylesheet">
<style>
  :root {
    --mat: #c6c8c7;
    --paper: #ffffff;
    --navy: #1d2d6b;
    --navy-deep: #16225a;
    --royal: #1e55c8;
    --sky-panel: #cbdff1;
    --ink: #18234f;
    --ink-soft: #3d3d3d;
    --pale: #d3e3f4;
    --rule: #c7d6ea;
  }
  * { margin: 0; padding: 0; box-sizing: border-box; }
  html, body { width: 952px; height: 1200px; overflow: hidden; }
  body { background: var(--mat); font-family: "Poppins", sans-serif; position: relative; }

  .poster {
    position: absolute; left: 73px; top: 78px; width: 806px; height: 1043px;
    background: var(--paper); overflow: hidden;
  }
  .archive-panel {
    position: absolute; left: 290px; top: 0; right: 0; bottom: 0;
    background: radial-gradient(ellipse at 62% 45%, #2c3f82 0%, var(--navy) 45%, var(--navy-deep) 100%);
  }
  .brand-box {
    position: absolute; left: 6px; top: 10px; width: 270px; height: 110px;
    background: var(--paper); border: 1px solid var(--rule);
    display: flex; flex-direction: column; align-items: center; justify-content: center;
  }
  .brand-name { font-weight: 600; font-size: 25px; color: var(--ink); letter-spacing: 0.2px; }
  .brand-tagline { margin-top: 6px; font-size: 11px; letter-spacing: 5.2px; color: var(--ink-soft); font-weight: 400; }

  .birthday-box {
    position: absolute; left: 276px; top: 10px; width: 281px; height: 110px;
    background: var(--sky-panel); overflow: hidden;
  }
  .birthday-box svg { position: absolute; left: 0; top: 0; }

  .portrait {
    position: absolute; left: 0; top: 135px; width: 478px; height: 908px;
    border-radius: 190px 190px 0 0;
    background: linear-gradient(180deg, #3b3a33 0%, #3b3a33 22%, #c9a591 32%, #f2f0ec 48%, #7a2631 62%, #f3f1ee 78%, #2c3550 100%);
    opacity: 0.9;
  }

  .headline { position: absolute; left: 499px; top: 0; color: var(--pale); }
  .headline span { position: absolute; left: 0; white-space: nowrap; line-height: 1; }
  .headline .lead { font-size: 40px; font-weight: 400; }
  .headline .big { font-size: 78px; font-weight: 300; letter-spacing: -0.5px; }
  .lead-1 { top: 480px; }
  .big-1 { top: 522px; }
  .lead-2 { top: 606px; }
  .big-2 { top: 648px; }

  .save-date {
    position: absolute; left: 486px; top: 772px; width: 110px;
    font-weight: 800; font-style: italic; font-size: 33px; line-height: 29px;
    color: var(--pale); text-align: right; letter-spacing: -0.5px;
  }
  .event-details { position: absolute; left: 600px; top: 780px; color: var(--pale); font-size: 13px; line-height: 1.15; }
  .detail { position: absolute; display: flex; align-items: flex-start; gap: 6px; white-space: nowrap; }
  .detail svg { flex: none; margin-top: 2px; }
  .detail-date { left: 14px; top: 0; }
  .detail-place { left: 4px; top: 26px; }
  .detail-mail { left: -4px; top: 66px; }

  .surprise {
    position: absolute; left: 488px; top: 885px; width: 294px;
    border-top: 1px solid var(--pale); border-bottom: 1px solid var(--pale);
    padding: 4px 0 5px; text-align: center;
    font-size: 12.5px; font-weight: 700; color: var(--pale); letter-spacing: 0.1px;
  }
  .roles { position: absolute; left: 522px; top: 947px; list-style: none; color: var(--pale); font-size: 13px; }
  .roles li { display: flex; align-items: center; gap: 8px; height: 23.5px; white-space: nowrap; }
  .roles strong { font-weight: 600; }
  .roles em { font-style: italic; font-weight: 300; }
</style>
</head>
<body>
  <main class="poster">
    <div class="archive-panel" role="img" aria-label="Faded navy-tinted archival photo of the founder in the early 1970s wearing a top hat and scarf"></div>

    <div class="brand-box">
      <div class="brand-name">Dell Pembrook</div>
      <div class="brand-tagline">GUIDE ON THE PATH</div>
    </div>

    <div class="birthday-box">
      <svg width="281" height="110" viewBox="0 0 281 110" aria-label="77th Birthday">
        <text x="8" y="108" font-family="Poppins, sans-serif" font-size="128" font-style="italic" font-weight="300" fill="none" stroke="#1e55c8" stroke-width="7" letter-spacing="-12">77</text>
        <text x="148" y="32" font-family="Poppins, sans-serif" font-size="12" font-weight="400" fill="#1e55c8">TH</text>
        <text x="34" y="73" font-family="Poppins, sans-serif" font-size="27" font-style="italic" font-weight="400" fill="#1e55c8" letter-spacing="11">BIRTHDAY</text>
      </svg>
    </div>

    <div class="portrait" role="img" aria-label="Present-day cut-out photo of the founder in a top hat, glasses, white shirt and burgundy paisley vest"></div>

    <h1 class="headline">
      <span class="lead lead-1">How it</span>
      <span class="big big-1">started,</span>
      <span class="lead lead-2">How it’s</span>
      <span class="big big-2">going</span>
    </h1>

    <div class="save-date">SAVE<br>THE<br>DATE</div>

    <div class="event-details">
      <div class="detail detail-date">
        <svg width="10" height="10" viewBox="0 0 10 10"><rect x="0.5" y="1.5" width="9" height="8" fill="none" stroke="#d3e3f4"/><line x1="0.5" y1="4" x2="9.5" y2="4" stroke="#d3e3f4"/><line x1="3" y1="0" x2="3" y2="2.5" stroke="#d3e3f4"/><line x1="7" y1="0" x2="7" y2="2.5" stroke="#d3e3f4"/></svg>
        <span>April 9</span>
      </div>
      <div class="detail detail-place">
        <svg width="10" height="11" viewBox="0 0 10 11"><path d="M5 0.5a3.5 3.5 0 0 1 3.5 3.5c0 2.5-3.5 6.5-3.5 6.5S1.5 6.5 1.5 4A3.5 3.5 0 0 1 5 0.5z" fill="#d3e3f4"/><circle cx="5" cy="4" r="1.3" fill="#1d2d6b"/></svg>
        <span>Marlow Ainsley Hall,<br>Austin Texas</span>
      </div>
      <div class="detail detail-mail">
        <svg width="11" height="9" viewBox="0 0 11 9"><rect x="0.5" y="0.5" width="10" height="8" fill="#d3e3f4"/><path d="M0.5 0.8 5.5 5 10.5 0.8" fill="none" stroke="#1d2d6b"/></svg>
        <span>team@guidewellpath.com</span>
      </div>
    </div>

    <p class="surprise">AND PLEASE REMEMBER THIS IS A SURPRISE!</p>

    <ul class="roles">
      <li><svg width="13" height="12" viewBox="0 0 13 12"><rect x="0.7" y="2.2" width="9" height="9" fill="none" stroke="#d3e3f4" stroke-width="1.3"/><path d="M3 6.3 5.3 8.6 12 1" fill="none" stroke="#d3e3f4" stroke-width="1.6"/></svg><span><strong>Author</strong> <em>(He’s published 2 books),</em></span></li>
      <li><svg width="13" height="12" viewBox="0 0 13 12"><rect x="0.7" y="2.2" width="9" height="9" fill="none" stroke="#d3e3f4" stroke-width="1.3"/><path d="M3 6.3 5.3 8.6 12 1" fill="none" stroke="#d3e3f4" stroke-width="1.6"/></svg><span><strong>Speaker</strong> <em>(A microphone),</em></span></li>
      <li><svg width="13" height="12" viewBox="0 0 13 12"><rect x="0.7" y="2.2" width="9" height="9" fill="none" stroke="#d3e3f4" stroke-width="1.3"/><path d="M3 6.3 5.3 8.6 12 1" fill="none" stroke="#d3e3f4" stroke-width="1.6"/></svg><span><strong>Business Coach, and Entrepreneur.</strong></span></li>
    </ul>
  </main>
</body>
</html>
```